Refer a Friend A5 Flyer for Healthcare Staff

We need an A5 flyer that we can hand out to existing and new staff members promoting our Refer a friend Scheme. We need the leaflet to encourage staff to talk to their family and friends about joining our Healthcare Agency, which provides staff to local care related establishments. Using our logo and brand colours blue and green, as per our website, the final design will need to clearly convey the benefits and attractions of referring additional staff to the team. In addition is the promotion of our Friendsbook page, requesting staff to like the page and to like and share various posts.

Target Market(s)

Healthcare and potential Healthcare Staff

Industry/Entity Type

Healthcare

Colors
33b8a4
3277b5

Requirements
Must have
• Company Logo, Brand colours,
• text; "Refer a Friend and receive a £50 Bonus after just 1 completed shift"
• text; "3 easy steps to refer a friend, 1 Fill out your name on the back of your Business Card 2 Hand the card to your friend or any person you wish to refer, 3 ask your friend to present the card to us when they attend their interview"
• text; "Like and share any of our Open Days on Friendsbook for a chance to win a prize, you can find us easily by searching @CarewellPlacementGroup"
• text; "Like our Page to stay up to date with our events and offers"
Nice to have
• care worker / elderly care / support worker pictures
• Content / pics from website www.carewellplacementgroup.co.uk

```html
<!DOCTYPE html>
<html lang="en">
<head>
<meta charset="utf-8">
<title>Refer a Friend – Carewell Placement</title>
<link rel="stylesheet" href="https://fonts.googleapis.com/css2?family=Open+Sans:wght@400;600;700;800&display=swap">
<style>
  :root {
    --brand-blue: #1d5ea9;
    --brand-blue-deep: #1a4f97;
    --brand-green: #33b8a4;
    --accent-orange: #f5a31a;
    --accent-orange-deep: #f08a1c;
    --swoosh-blue: #d5e3f0;
    --paper: #f3f3f5;
    --ink: #1e1e1e;
    --white: #ffffff;
    --photo-warm: #c9b3a0;
    --photo-light: #e9e0d5;
  }
  * { box-sizing: border-box; margin: 0; padding: 0; }
  html, body { width: 839px; height: 1200px; overflow: hidden; background: var(--paper); }
  body { font-family: "Open Sans", Arial, sans-serif; color: var(--ink); }

  .flyer { position: relative; width: 839px; height: 1200px; overflow: hidden; background: var(--paper); }

  .hero { position: absolute; left: 0; top: 0; width: 839px; height: 620px; }

  .offer { position: absolute; left: 40px; top: 612px; width: 420px; text-align: center; }
  .offer__title { color: var(--brand-blue); font-size: 41px; font-weight: 800; letter-spacing: 4px; line-height: 1; }
  .offer__line { font-size: 16px; font-weight: 600; letter-spacing: 2.5px; text-transform: uppercase; }
  .offer__line--receive { margin-top: 22px; }
  .offer__bonus { color: var(--accent-orange); font-weight: 800; line-height: 1; margin-top: 2px; }
  .offer__bonus .amount { font-size: 44px; }
  .offer__bonus .amount sup { font-size: 24px; vertical-align: 14px; }
  .offer__bonus .word { font-size: 34px; letter-spacing: 1px; }
  .offer__line--shift { margin-top: 6px; }
  .offer__line--shift .num { font-size: 22px; font-weight: 700; }

  .brand { position: absolute; left: 495px; top: 660px; display: flex; align-items: center; gap: 12px; }
  .brand__mark { width: 26px; height: 26px; border-radius: 50%; background: var(--brand-green); }
  .brand__name { color: var(--brand-blue); font-size: 34px; font-weight: 600; line-height: 1; }

  .divider { position: absolute; left: 68px; top: 799px; width: 703px; height: 2px; background: var(--brand-blue); }

  .steps-title { position: absolute; left: 0; top: 810px; width: 839px; text-align: center;
    color: var(--accent-orange); font-size: 24px; font-weight: 800; letter-spacing: 1.5px; text-transform: uppercase; }

  .step { position: absolute; top: 872px; width: 240px; }
  .step__num { position: absolute; left: 0; top: 0; width: 24px; height: 24px; border-radius: 50%;
    background: var(--brand-blue-deep); color: var(--white); font-size: 10px; font-weight: 600;
    display: flex; align-items: center; justify-content: center; }
  .step__text { padding-top: 28px; font-size: 19px; line-height: 1.5; text-align: center; }
  .step--one { left: 36px; }
  .step--two { left: 297px; }
  .step--three { left: 553px; }
  .step__rule { position: absolute; top: 855px; width: 2px; height: 135px;
    border-left: 2px dotted var(--brand-green); }

  .footer-band { position: absolute; left: 0; top: 1020px; width: 839px; height: 180px; }
  .footer { position: absolute; left: 210px; top: 1090px; width: 610px; color: var(--white); font-size: 16px; line-height: 1.4; }
  .footer__follow { margin-top: 2px; font-variant: small-caps; letter-spacing: 0.6px; font-size: 17px; }
  .like-badge { position: absolute; left: 98px; top: 1072px; width: 96px; height: 72px; border-radius: 8px;
    background: var(--white); color: var(--brand-blue); font-weight: 800; font-size: 17px; line-height: 1.05;
    display: flex; flex-direction: column; align-items: center; justify-content: center; text-align: center; }
</style>
</head>
<body>
<main class="flyer">

  <svg class="hero" viewBox="0 0 839 620" xmlns="http://www.w3.org/2000/svg">
    <defs>
      <linearGradient id="photoTone" x1="0" y1="0" x2="1" y2="1">
        <stop offset="0" stop-color="var(--photo-light)"/>
        <stop offset="0.5" stop-color="var(--photo-warm)"/>
        <stop offset="1" stop-color="#f0eeea"/>
      </linearGradient>
    </defs>
    <path role="img" aria-label="Photo: smiling care worker in a white uniform walking arm in arm with an elderly woman"
          d="M0,0 H839 V566 C620,570 430,540 300,470 C170,400 70,300 0,180 Z" fill="url(#photoTone)"/>
    <path d="M0,250 C140,470 420,580 839,582 V592 C420,600 120,500 0,300 Z" fill="var(--swoosh-blue)"/>
    <path d="M0,95 C40,260 150,420 330,522 C170,450 60,330 0,190 Z" fill="var(--accent-orange)"/>
    <path d="M0,110 C30,240 110,370 250,468 C120,400 40,300 0,200 Z" fill="var(--accent-orange-deep)" opacity="0.6"/>
  </svg>

  <section class="offer">
    <h1 class="offer__title">REFER A FRIEND</h1>
    <p class="offer__line offer__line--receive">and receive a</p>
    <p class="offer__bonus"><span class="amount"><sup>£</sup>50</span> <span class="word">BONUS</span></p>
    <p class="offer__line offer__line--shift">after just <span class="num">1</span> completed shift</p>
  </section>

  <div class="brand">
    <span class="brand__mark"></span>
    <span class="brand__name">Carewell<br>Placement</span>
  </div>

  <div class="divider"></div>
  <h2 class="steps-title">3 easy steps to refer a friend</h2>

  <div class="step step--one">
    <span class="step__num">01</span>
    <p class="step__text">Fill out your name on the back of your Business Card</p>
  </div>
  <span class="step__rule" style="left:268px"></span>

  <div class="step step--two">
    <span class="step__num">02</span>
    <p class="step__text">Hand the card to your friend or any person you wish to refer</p>
  </div>
  <span class="step__rule" style="left:529px"></span>

  <div class="step step--three">
    <span class="step__num">03</span>
    <p class="step__text">Ask your friend to present the card to us when they attend their interview</p>
  </div>
  <span class="step__rule" style="left:800px"></span>

  <svg class="footer-band" viewBox="0 0 839 180" xmlns="http://www.w3.org/2000/svg">
    <path d="M0,60 C250,0 590,0 839,60 V180 H0 Z" fill="var(--accent-orange)"/>
    <path d="M0,58 C250,6 590,6 839,70 V180 H0 Z" fill="var(--brand-green)"/>
    <path d="M0,75 C250,22 590,22 839,90 V180 H0 Z" fill="var(--brand-blue)"/>
  </svg>

  <div class="like-badge">LIKE<br>&amp; SHARE</div>

  <div class="footer">
    <p>any of our Open Days on Friendsbook for a chance to win a prize, you can find us easily by searching @CarewellPlacementGroup</p>
    <p class="footer__follow">Like our Page to stay up to date with our events and offers</p>
  </div>

</main>
</body>
</html>
```